Design Website appearance

Seeking someone to provide ideas on matters of color and contrast for the current design of the website.
Ideas top menu types and menu navigation.

https://www.filevarko.net/s/7kq4mwtzpe9bhxd/Esqueleto%20de%20Interface.pdf

Target Market(s)

We sell consulting services Information Systems for medium and small businesses.

```html
<!DOCTYPE html>
<html lang="en">
<head>
<meta charset="utf-8">
<title>Contact</title>
<link href="https://fonts.googleapis.com/css2?family=Mulish:wght@300;400;500&display=swap" rel="stylesheet">
<style>
  :root {
    --brand: #fdc300;
    --ink: #6f6f6f;
    --ink-soft: #8a8a8a;
    --line: #c9c9c9;
    --page: #ffffff;
    --footer: #222222;
    --footer-text: #ffffff;
    --footer-muted: #7b7b7b;
    --social: #555555;
  }
  * { box-sizing: border-box; margin: 0; padding: 0; }
  html, body { width: 1000px; height: 1200px; overflow: hidden; background: var(--page); }
  body { position: relative; font-family: 'Mulish', sans-serif; color: var(--ink); }
  .abs { position: absolute; }

  .brand-mark { left: 70px; top: 20px; width: 144px; height: 107px; background: var(--brand);
    color: #fff; font-size: 40px; font-weight: 400; display: flex; align-items: center; justify-content: center; letter-spacing: 0.5px; }

  .main-nav { right: 70px; top: 62px; display: flex; gap: 29px; font-size: 15.5px; color: var(--ink); }
  .main-nav a { color: inherit; text-decoration: none; position: relative; }
  .nav-indicator { left: 514px; top: 0; width: 146px; height: 3px; background: var(--brand); }

  .hero-slide { left: 70px; top: 151px; width: 860px; height: 334px;
    background: linear-gradient(100deg, #1a2634 0%, #5f7590 22%, #c9d3de 40%, #e8ecf1 60%, #2a3f62 80%, #dfe5ee 100%); }
  .slide-arrow { top: 296px; }
  .slider-dots { left: 855px; top: 490px; display: flex; align-items: center; gap: 10px; }
  .slider-dots span { width: 10px; height: 10px; border-radius: 50%; background: var(--brand); }
  .slider-dots span.is-active { width: 14px; height: 14px; }

  .contact-icon { left: 70px; top: 592px; }
  .contact-title { left: 129px; top: 585px; font-size: 28px; font-weight: 400; color: var(--ink-soft); }

  .field { border: 2px solid var(--line); background: #fff; font-size: 15px; color: var(--ink);
    display: flex; align-items: center; padding-left: 21px; }
  .field.is-focused { border-color: var(--brand); }
  .caret { display: inline-block; width: 1.5px; height: 19px; background: var(--brand); margin-left: 1px; }
  .field-name { left: 130px; top: 648px; width: 365px; height: 46px; }
  .field-email { left: 130px; top: 714px; width: 365px; height: 46px; }
  .field-subject { left: 130px; top: 780px; width: 365px; height: 46px; }
  .select-arrow { right: 18px; top: 17px; }
  .field-message { left: 515px; top: 648px; width: 355px; height: 178px; }
  .send-button { left: 772px; top: 846px; width: 98px; height: 46px; border: 2px solid var(--line);
    display: flex; align-items: center; justify-content: center; font-size: 15px; color: var(--ink); }

  .site-footer { left: 0; top: 916px; width: 1000px; height: 284px; background: var(--footer); }
  .footer-links { left: 70px; top: 954px; display: flex; gap: 11px; font-size: 9px; }
  .footer-links a { color: var(--brand); text-decoration: underline; }
  .social-list { left: 70px; top: 1037px; display: flex; gap: 29px; }
  .social-list span { width: 31px; height: 31px; border-radius: 50%; background: var(--social); }
  .social-list span.is-hover { background: #fff; }
  .sr-only { position: absolute; width: 1px; height: 1px; overflow: hidden; clip: rect(0 0 0 0); }
  .copyright { left: 70px; top: 1147px; font-size: 13px; font-weight: 300; color: var(--footer-muted); }

  .contact-block { left: 490px; }
  .contact-block h3 { position: absolute; left: 28px; top: 0; font-size: 15px; font-weight: 400; color: var(--footer-text); white-space: nowrap; }
  .contact-block p { position: absolute; left: 29px; font-size: 11.5px; font-weight: 300; color: var(--footer-muted); line-height: 14.5px; white-space: nowrap; }
  .contact-block p strong { font-weight: 300; color: #bdbdbd; }

  .map-frame { left: 644px; top: 954px; width: 286px; height: 209px; background: #fff; border-radius: 4px; padding: 5px; }
  .map-area { width: 100%; height: 100%; background: linear-gradient(135deg, #e6e2d6 0%, #d9dccb 45%, #e9e5da 100%); }
</style>
</head>
<body>
  <div class="abs nav-indicator"></div>
  <div class="abs brand-mark">LOGO</div>
  <nav class="abs main-nav">
    <a href="#">Services</a>
    <a href="#">Project Management</a>
    <a href="#">Business Architecture</a>
    <a href="#">Initiation</a>
  </nav>

  <div class="abs hero-slide" role="img" aria-label="Photo of hands holding a pen and a printed document at a business meeting"></div>
  <svg class="abs slide-arrow" style="left:80px" width="16" height="44" viewBox="0 0 16 44"><polyline points="14,1 2,22 14,43" fill="none" stroke="var(--brand)" stroke-width="2"/></svg>
  <svg class="abs slide-arrow" style="left:904px" width="16" height="44" viewBox="0 0 16 44"><polyline points="2,1 14,22 2,43" fill="none" stroke="var(--brand)" stroke-width="2"/></svg>
  <div class="abs slider-dots"><span></span><span></span><span class="is-active"></span><span></span></div>

  <svg class="abs contact-icon" width="28" height="22" viewBox="0 0 28 22">
    <rect x="0" y="0" width="28" height="22" fill="var(--brand)"/>
    <polyline points="1,2 14,13 27,2" fill="none" stroke="#fff" stroke-width="2.5"/>
    <line x1="1" y1="21" x2="10" y2="11" stroke="#fff" stroke-width="2"/>
    <line x1="27" y1="21" x2="18" y2="11" stroke="#fff" stroke-width="2"/>
  </svg>
  <h2 class="abs contact-title">Drop us a line or two!</h2>

  <div class="abs field field-name is-focused">Marten Eschelby<span class="caret"></span></div>
  <div class="abs field field-email">Email address</div>
  <div class="abs field field-subject">Subject
    <svg class="abs select-arrow" width="12" height="9" viewBox="0 0 12 9"><polygon points="0,0 12,0 6,9" fill="var(--brand)"/></svg>
  </div>
  <div class="abs field field-message"></div>
  <div class="abs send-button">SEND</div>

  <footer class="abs site-footer"></footer>
  <div class="abs footer-links">
    <a href="#">MIDDLEWARE</a><a href="#">APPLICATIONS</a><a href="#">DATABASE</a><a href="#">RESOURCES</a><a href="#">NEWS</a>
  </div>
  <div class="abs social-list">
    <span><i class="sr-only">Linkora</i></span>
    <span><i class="sr-only">Vidstream</i></span>
    <span><i class="sr-only">Chirpline</i></span>
    <span class="is-hover"><i class="sr-only">Circlet</i></span>
    <span><i class="sr-only">Friendwall</i></span>
  </div>
  <div class="abs copyright">© All rights reserved Norvale Corporation 2003 - 2013</div>

  <div class="abs contact-block" style="top:955px">
    <svg class="abs" style="left:0;top:0" width="16" height="16" viewBox="0 0 16 16"><path d="M3 0 L6 4 L4.5 6 Q6.5 10 10 11.5 L12 10 L16 13 L14 16 Q5 15 0 3 Z" fill="var(--brand)"/></svg>
    <h3>Phone</h3>
    <p style="top:29px">Call to:<br><strong>+1 555-214-0388</strong><br>Call to:<br><strong>5550142</strong></p>
  </div>
  <div class="abs contact-block" style="top:1052px">
    <svg class="abs" style="left:2px;top:1px" width="14" height="14" viewBox="0 0 14 14"><circle cx="7" cy="7" r="7" fill="var(--brand)"/></svg>
    <h3>Callnet</h3>
    <p style="top:28px">Tallis 204</p>
  </div>
  <div class="abs contact-block" style="top:1109px">
    <svg class="abs" style="left:2px;top:0" width="13" height="17" viewBox="0 0 13 17"><path d="M6.5 0 A6.5 6.5 0 0 1 13 6.5 C13 11 6.5 17 6.5 17 C6.5 17 0 11 0 6.5 A6.5 6.5 0 0 1 6.5 0 Z" fill="var(--brand)"/><circle cx="6.5" cy="6.5" r="2.3" fill="var(--footer)"/></svg>
    <h3>Address</h3>
    <p style="top:27px">00412 Marlow Bay,<br>Port Evren</p>
  </div>

  <div class="abs map-frame"><div class="map-area" role="img" aria-label="Street map of the office neighbourhood"></div></div>
</body>
</html>
```